Graphic Banner Design - 2.5' x 6' - High Tech Company

We are in need of a banner design for an outdoor sign that will be used at sponsorship events.

Size
2.5' x 6'

The company is a high tech company, and the design will be used for action sports events. So lining up to that would be good.

Tag line to be incorporated...
"Extreme IT Services for Extreme Needs."

Target Market(s)

Business Owners, Entrepreneurs, IT Professionals.

Industry/Entity Type

Information Technology

Logo Text

Brindlex

Colors

Designer to choose colors to be used in the design.

Requirements
Must have
• Must feel young and vibrant, fit in to an action sports event and just be out of this world awesome.
• In the world of the IT, we are the Castavelli. Fast, Awesome, not necessarily cheap, but you know it will do what you want extremely well. Not for everyone, but always desired.

```html
<!DOCTYPE html>
<html lang="en">
<head>
<meta charset="utf-8">
<title>Brindlex Event Banner</title>
<link rel="stylesheet" href="https://fonts.googleapis.com/css2?family=Montserrat:wght@400&family=PT+Sans+Narrow:wght@700&display=swap">
<style>
  :root {
    --page-bg: #e9ecef;
    --panel-dark: #3f3f41;
    --panel-light: #e6e6e8;
    --brand-blue: #2457da;
    --ink-dark: #333335;
    --white: #ffffff;
    --photo-glow: #f2f6ff;
    --photo-beam: #9fb8ff;
    --photo-blue: #4f6fe0;
    --photo-violet: #4a3f9e;
    --photo-deep: #141830;
  }
  * { margin: 0; padding: 0; box-sizing: border-box; }
  html, body {
    width: 1200px; height: 840px; overflow: hidden;
    background: var(--page-bg);
  }
  .banner {
    position: absolute; left: 20px; top: 192px;
    width: 1160px; height: 455px;
    overflow: hidden;
    box-shadow: 0 6px 18px rgba(0,0,0,.18);
  }
  .banner-shapes { position: absolute; inset: 0; }
  .brand-name {
    position: absolute; left: 740px; width: 420px; top: 84px;
    text-align: center;
    font-family: "Montserrat", sans-serif; font-weight: 400;
    font-size: 40px; line-height: 48px; letter-spacing: .5px; color: var(--white);
  }
  .tagline {
    position: absolute; left: 760px; width: 360px; top: 166px;
    text-align: center;
    font-family: "PT Sans Narrow", sans-serif; font-weight: 700;
    font-size: 50px; line-height: 49px; color: var(--ink-dark);
    text-transform: uppercase;
  }
  .tagline span { display: block; }
  .tagline .accent { color: var(--brand-blue); }
  .web-address {
    position: absolute; left: 518px; width: 630px; top: 368px; height: 78px;
    display: flex; align-items: center; gap: 10px;
    font-family: "Montserrat", sans-serif; font-weight: 400;
    font-size: 41px; color: var(--white);
  }
  .web-address svg { flex: none; }
</style>
</head>
<body>
  <section class="banner">
    <svg class="banner-shapes" width="1160" height="455" viewBox="0 0 1160 455" xmlns="http://www.w3.org/2000/svg">
      <defs>
        <linearGradient id="stage-base" x1="0" y1="0" x2="0" y2="1">
          <stop offset="0" stop-color="var(--photo-violet)"/>
          <stop offset="0.45" stop-color="var(--photo-blue)"/>
          <stop offset="0.72" stop-color="#2c2f5e"/>
          <stop offset="1" stop-color="var(--photo-deep)"/>
        </linearGradient>
        <radialGradient id="stage-glow" cx="0.42" cy="0.3" r="0.55">
          <stop offset="0" stop-color="var(--photo-glow)" stop-opacity="0.95"/>
          <stop offset="0.35" stop-color="var(--photo-beam)" stop-opacity="0.7"/>
          <stop offset="1" stop-color="var(--photo-beam)" stop-opacity="0"/>
        </radialGradient>
      </defs>
      <g class="event-photo" role="img" aria-label="Excited concert crowd with raised arms in front of a band on a stage lit by bright spotlights">
        <rect x="0" y="0" width="1160" height="455" fill="url(#stage-base)"/>
        <rect x="0" y="0" width="1160" height="455" fill="url(#stage-glow)"/>
      </g>
      <polygon class="panel-light" points="767,148 1160,148 1160,455 640,455" fill="var(--panel-light)"/>
      <polygon class="stripe-blue" points="755,148 769,148 693,370 679,370" fill="var(--brand-blue)"/>
      <polygon class="stripe-white" points="718,190 729,190 645,455 634,455" fill="var(--white)"/>
      <polygon class="panel-dark" points="752,0 1160,0 1160,148 727,148" fill="var(--panel-dark)"/>
      <polygon class="band-blue" points="512,370 1160,374 1160,448 490,448" fill="var(--brand-blue)"/>
    </svg>

    <div class="brand-name">Brindlex</div>

    <h1 class="tagline">
      <span>Extreme</span>
      <span class="accent">IT Services</span>
      <span>For Extreme</span>
      <span>Needs</span>
    </h1>

    <div class="web-address">
      <svg width="36" height="36" viewBox="0 0 36 36" aria-hidden="true">
        <g fill="none" stroke="var(--white)" stroke-width="2">
          <circle cx="18" cy="18" r="15"/>
          <ellipse cx="18" cy="18" rx="7" ry="15"/>
          <line x1="3" y1="18" x2="33" y2="18"/>
          <line x1="18" y1="3" x2="18" y2="33"/>
          <path d="M6 10h24M6 26h24"/>
        </g>
      </svg>
      <span>www.brindlex.com</span>
    </div>
  </section>
</body>
</html>
```